Celebrate February in The Smokies at Maple Hollow Splashpark Lodge

Create something similar to the attached design - can very and be creative but the overall concept is one I would like to recreate
Celebrate February in The Smokies
Maple Hollow logo (at top)
Romantic Rooms, Family Suites, Free Buffet Breakfast included, Indoor Pool and Parkway Convenience
Low Rates!

866.214.5093 MapleHollowLodge.example/

I have attached logos and pictures to use

Target Market(s)

Email customers to entice them to come to the smokies in February ..

Industry/Entity Type

Hospitality

Requirements
Must have
• phone number 866.214.5093
• website MapleHollowLodge.example/
Nice to have
• a romantic feel but not to much so .. families and couples can both enjoy the area in february

```html
<!DOCTYPE html>
<html lang="en">
<head>
<meta charset="utf-8">
<title>Celebrate February in the Smokies – Maple Hollow Splashpark Lodge</title>
<link rel="stylesheet" href="https://fonts.googleapis.com/css2?family=Anton&family=Oswald:wght@500&family=Noto+Serif:wght@400;700&family=Arimo:wght@700&display=swap">
<style>
  :root {
    --backdrop: #bf7fe0;
    --card: #f4f5f7;
    --card-band: #b3b3b3;
    --navy: #0c1a8c;
    --ink: #111111;
    --slate: #444444;
    --heat-start: #ffb534;
    --heat-end: #ff5f7e;
  }
  * { box-sizing: border-box; margin: 0; padding: 0; }
  html, body {
    width: 923px; height: 1200px; overflow: hidden;
    background: var(--backdrop);
  }
  .door-hanger {
    position: absolute;
    left: 270px; top: 51px;
    width: 383px; height: 1098px;
  }
  .hanger-shape { position: absolute; inset: 0; filter: drop-shadow(0 6px 10px rgba(60,20,90,.25)); }
  .brand {
    position: absolute; top: 36px; left: 0; width: 100%;
    display: flex; align-items: center; justify-content: center; gap: 10px;
  }
  .brand-dot { width: 34px; height: 34px; border-radius: 50%; background: #2a9fd6; flex: none; }
  .brand-name {
    font-family: "Noto Serif", serif; font-weight: 700; font-size: 22px;
    line-height: 1.1; color: var(--navy);
  }
  .headline {
    position: absolute; top: 395px; left: 22px; width: 345px;
    transform: rotate(-5deg); transform-origin: left top;
    font-family: "Anton", sans-serif; text-transform: uppercase;
    font-size: 66px; line-height: 0.98; letter-spacing: 0.5px;
    background: linear-gradient(100deg, var(--heat-start), var(--heat-end));
    -webkit-background-clip: text; background-clip: text; color: transparent;
  }
  .headline span { display: block; }
  .headline .line-two { padding-left: 12px; }
  .tagline {
    position: absolute; top: 492px; right: 38px;
    font-family: "Oswald", sans-serif; font-weight: 500; font-size: 27px;
    color: var(--slate); letter-spacing: -0.5px; text-transform: uppercase;
  }
  .room-photo {
    position: absolute; left: 30px; top: 560px; width: 319px; height: 178px;
    background: linear-gradient(90deg, #6b5a48 0%, #efe1c2 35%, #f4ead4 65%, #ddd6cc 100%);
  }
  .amenities {
    position: absolute; top: 758px; left: 30px; width: 323px;
    font-family: "Noto Serif", serif; font-size: 22px; line-height: 30.5px;
    text-align: center; color: var(--ink);
  }
  .offer {
    position: absolute; top: 928px; left: 0; width: 100%; text-align: center;
    font-family: "Noto Serif", serif; font-weight: 700; font-size: 21px;
    letter-spacing: 1px; color: var(--ink);
  }
  .contact {
    position: absolute; top: 983px; left: 0; width: 100%; text-align: center;
    font-family: "Arimo", sans-serif; font-weight: 700;
  }
  .phone { font-size: 40px; line-height: 1; color: var(--navy); }
  .website { font-size: 21px; margin-top: 6px; color: var(--ink); }
</style>
</head>
<body>
  <div class="door-hanger">
    <svg class="hanger-shape" width="383" height="1098" viewBox="0 0 383 1098" aria-hidden="true">
      <defs>
        <clipPath id="hanger-outline">
          <path d="M12 0 H371 A12 12 0 0 1 383 12 V1086 A12 12 0 0 1 371 1098 H12 A12 12 0 0 1 0 1086 V392 A14 14 0 0 1 10 378 L160 290 A58 58 0 1 1 150 185 L10 170 A12 12 0 0 1 0 158 V12 A12 12 0 0 1 12 0 Z"/>
        </clipPath>
      </defs>
      <g clip-path="url(#hanger-outline)">
        <rect width="383" height="1098" fill="var(--card)"/>
        <rect y="1066" width="383" height="32" fill="var(--card-band)"/>
      </g>
    </svg>

    <div class="brand">
      <span class="brand-dot"></span>
      <span class="brand-name">Maple Hollow<br>Splashpark Lodge</span>
    </div>

    <h1 class="headline"><span>Celebrate</span><span class="line-two">February</span></h1>
    <p class="tagline">In the Smokies</p>

    <div class="room-photo" role="img" aria-label="Bright lodge suite with a large bed, arched mountain window and a jetted tub"></div>

    <p class="amenities">Romantic Rooms, Family Suites, Free Buffet Breakfast included, Indoor Pool and Parkway Convenience</p>
    <p class="offer">LOW RATES !</p>

    <div class="contact">
      <p class="phone">866.214.5093</p>
      <p class="website">MapleHollowLodge.example/</p>
    </div>
  </div>
</body>
</html>
```